serious, thorough, light and simple - that's my advice and mediations

My business card should combine my logo (uploaded file) and my homepage (https://fellor-mediation.webnestsite.com).

Contact Information for Business Card

Name: Sabine Fellor di Vanti
Phone: 076 412 58 94
mail: sfellor@postkiv.ch
web: www.fellor-di-vanti.ch

```html
<!DOCTYPE html>
<html lang="de">
<head>
<meta charset="utf-8">
<title>Wege im Dialog – Visitenkarte</title>
<link href="https://fonts.googleapis.com/css2?family=Roboto:wght@400;500&display=swap" rel="stylesheet">
<style>
  :root {
    --backdrop: #1e1e1f;
    --royal-blue: #283d8f;
    --royal-blue-light: #3a4f9e;
    --paper: #ffffff;
    --gold: #b08a55;
    --text-light: #ffffff;
  }
  html, body {
    margin: 0;
    padding: 0;
    width: 1200px;
    height: 930px;
    overflow: hidden;
    background: var(--backdrop);
    font-family: "Roboto", Arial, sans-serif;
  }
  .canvas {
    position: relative;
    width: 1200px;
    height: 930px;
  }
  .card {
    position: absolute;
    width: 540px;
    height: 316px;
    border-radius: 22px;
    overflow: hidden;
    box-shadow: 0 18px 40px rgba(0,0,0,0.45);
  }
  .card-front {
    left: 90px;
    top: 110px;
    background: linear-gradient(115deg, var(--royal-blue) 0%, var(--royal-blue-light) 55%, var(--royal-blue) 100%);
    display: flex;
    align-items: center;
    justify-content: center;
  }
  .card-back {
    left: 570px;
    top: 490px;
    background: var(--royal-blue);
  }
  .card-back svg.shape {
    position: absolute;
    inset: 0;
  }
  .brand {
    display: flex;
    align-items: center;
    gap: 14px;
    font-weight: 400;
    letter-spacing: 0.04em;
  }
  .brand-dot {
    width: 26px;
    height: 26px;
    border-radius: 50%;
  }
  .card-front .brand { color: var(--text-light); font-size: 40px; }
  .card-front .brand-dot { background: var(--text-light); }
  .card-back .brand {
    position: absolute;
    right: 40px;
    top: 70px;
    color: var(--gold);
    font-size: 30px;
  }
  .card-back .brand-dot { background: var(--gold); width: 20px; height: 20px; }
  .contact {
    position: absolute;
    left: 38px;
    bottom: 30px;
    color: var(--text-light);
  }
  .contact-name { font-size: 20px; font-weight: 500; margin: 0; }
  .contact-role { font-size: 14px; margin: 2px 0 14px; opacity: 0.9; }
  .contact-list { list-style: none; margin: 0; padding: 0; font-size: 15px; }
  .contact-list li { display: flex; align-items: center; gap: 8px; line-height: 23px; }
  .contact-list svg { width: 12px; height: 12px; fill: none; stroke: var(--text-light); stroke-width: 2; }
</style>
</head>
<body>
<main class="canvas">
  <section class="card card-front" aria-label="Vorderseite">
    <div class="brand"><span class="brand-dot"></span>Wege im Dialog</div>
  </section>

  <section class="card card-back" aria-label="Rückseite">
    <svg class="shape" viewBox="0 0 540 316" width="540" height="316" aria-hidden="true">
      <path d="M120 0 Q210 250 540 240 L540 0 Z" fill="var(--paper)"/>
      <path d="M120 0 Q210 250 540 240" fill="none" stroke="var(--gold)" stroke-width="4"/>
    </svg>
    <div class="brand"><span class="brand-dot"></span>Wege im Dialog</div>
    <div class="contact">
      <p class="contact-name">Sabine Fellor di Vanti</p>
      <p class="contact-role">Director</p>
      <ul class="contact-list">
        <li><svg viewBox="0 0 12 12"><path d="M2 1 L4 1 L5 4 L3.5 5 Q5 8 7 8.5 L8 7 L11 8 L11 10 Q6 11 1.5 5 Q1 3 2 1 Z"/></svg>076 412 58 94</li>
        <li><svg viewBox="0 0 12 12"><rect x="1" y="2.5" width="10" height="7"/><path d="M1 2.5 L6 6.5 L11 2.5"/></svg>sfellor@postkiv.ch</li>
        <li><svg viewBox="0 0 12 12"><circle cx="6" cy="6" r="5"/><path d="M1 6 H11 M6 1 Q3 6 6 11 M6 1 Q9 6 6 11"/></svg>www.fellor-di-vanti.ch</li>
      </ul>
    </div>
  </section>
</main>
</body>
</html>
```